verdant harbour requires some business cards

I need some business cards created that feature the company's newly designed logo. The business cards need to be be double sided and be a standard Australian size of 90mm x 55mm

Target Market(s)

business professionals, company executives, local goverment

Industry/Entity Type

Business

Requirements
Must have
• Company's logo
• The information section must include
• Individual name:
• Position:
• Phone:
• Address:
• Email:
• Website: www.verdantharbour.example
• The cards need to be easily formatted so I can enter staff members details positions etc...
• I plan to get these printed at deskmarket so can you please ensure that all designs meet their printing requirements http://www.deskmarket.example/retail/b2c/opsProductCreate.do?qty=1&cardQty=1000&sided=double&productname=colourbusinesscards&category=businesscards
Nice to have
• I might like to see some of the services we offer printed on one of the faces:
• Lighting Design (architectural, commercial, residential, theatrical ,exterior, interior) Lighting Consultancy, Theatrical Consultancy

```html
<!DOCTYPE html>
<html lang="en">
<head>
<meta charset="utf-8">
<title>verdant harbour business cards</title>
<link href="https://fonts.googleapis.com/css2?family=Questrial&family=Open+Sans:wght@400&display=swap" rel="stylesheet">
<style>
  :root {
    --page: #e9e7e3;
    --card: #1c1c1d;
    --card-edge: #151516;
    --blue: #1fa3dc;
    --white: #f4f4f4;
    --ink-dark: #10222c;
    --muted: #d8d8d8;
    --green: #8cc63f;
  }
  * { margin: 0; padding: 0; box-sizing: border-box; }
  html, body { width: 1200px; height: 1000px; overflow: hidden; }
  body {
    background: var(--page);
    font-family: "Questrial", sans-serif;
    position: relative;
  }
  .card {
    position: absolute;
    left: 300px;
    width: 600px;
    height: 367px;
    background: var(--card);
    border-radius: 34px 4px 34px 4px;
    overflow: hidden;
    box-shadow: 0 6px 18px rgba(0,0,0,0.25);
  }
  .card--front { top: 100px; }
  .card--back { top: 520px; }

  .name-band {
    position: absolute;
    left: 0; top: 42px;
    width: 440px; height: 30px;
    background: var(--blue);
    display: flex; align-items: flex-end;
    padding: 0 0 4px 30px;
    gap: 8px;
  }
  .name-band__name { color: var(--white); font-size: 22px; line-height: 1; }
  .name-band__credentials { color: var(--ink-dark); font-size: 12px; line-height: 1.2; }
  .position { position: absolute; left: 32px; top: 82px; color: var(--white); font-size: 12px; }

  .brand {
    position: absolute;
    display: flex; align-items: center; gap: 10px;
    color: var(--white);
    white-space: nowrap;
  }
  .brand__dot { border-radius: 50%; background: var(--blue); flex: none; }
  .card--front .brand { left: 34px; top: 160px; font-size: 34px; }
  .card--front .brand__dot { width: 22px; height: 22px; }
  .card--back .brand { left: 0; right: 0; justify-content: center; top: 120px; font-size: 56px; }
  .card--back .brand__dot { width: 34px; height: 34px; }

  .tagline {
    position: absolute; left: 0; right: 0; top: 205px;
    text-align: center; color: var(--white);
    font-size: 17px; letter-spacing: 4px;
  }

  .contacts {
    position: absolute; left: 28px; bottom: 40px;
    list-style: none;
    font-family: "Open Sans", sans-serif;
    font-size: 11px; letter-spacing: 1.6px; color: var(--muted);
  }
  .contacts li { display: flex; align-items: center; gap: 6px; line-height: 16px; }
  .contacts svg { width: 11px; height: 11px; fill: var(--green); flex: none; }

  .edge-strip {
    position: absolute; left: 0; bottom: 0;
    width: 100%; height: 14px;
    background: linear-gradient(90deg, var(--blue) 0%, var(--blue) 40%, rgba(31,163,220,0) 100%);
  }
</style>
</head>
<body>
  <section class="card card--front" aria-label="Business card front">
    <div class="name-band">
      <span class="name-band__name">Daniel Ashcombe</span>
      <span class="name-band__credentials">MLighting, BMA, Assoc LDA</span>
    </div>
    <p class="position">Director</p>

    <div class="brand"><span class="brand__dot"></span><span>verdant harbour</span></div>

    <ul class="contacts">
      <li><svg viewBox="0 0 12 12"><path d="M2 1l2 0 1 3-1.5 1a7 7 0 0 0 3.5 3.5L8 7l3 1v2c0 1-1 1-1 1A9 9 0 0 1 1 2s0-1 1-1z"/></svg>+61 8 5550 1234</li>
      <li><svg viewBox="0 0 12 12"><path d="M0 2h12v8H0z M1 3l5 4 5-4" stroke="#1c1c1d" stroke-width="1"/></svg>daniel@verdantharbour.example</li>
      <li><svg viewBox="0 0 12 12"><circle cx="6" cy="6" r="5.5"/></svg>www.verdantharbour.example</li>
      <li><svg viewBox="0 0 12 12"><path d="M6 0l6 5.5h-2V12H7.5V8h-3v4H2V5.5H0z"/></svg>PO Box 482, Eastvale WA 6999 Australia</li>
    </ul>
    <div class="edge-strip"></div>
  </section>

  <section class="card card--back" aria-label="Business card back">
    <div class="brand"><span class="brand__dot"></span><span>verdant harbour</span></div>
    <p class="tagline">Lighting Design &amp; Consultancy</p>
    <div class="edge-strip"></div>
  </section>
</body>
</html>
```